Step and Repeat Backdrop for wedding reception photo booth

Would like to have a Step and Repeat Backdrop (8 foot high by 10 foot wide) that incorporates the wedding logo (attached) and the names Elena and Gavin. Background should be white, and wedding colors are burgundy and gold. Show me creativity :-) I have included some random samples.

```html
<!DOCTYPE html>
<html lang="en">
<head>
<meta charset="utf-8">
<title>Elena &amp; Gavin — Step and Repeat Backdrop</title>
<link rel="stylesheet" href="https://fonts.googleapis.com/css2?family=Marcellus&display=swap">
<style>
  :root {
    --burgundy: #8c1a3c;
    --gold: #b8933f;
    --paper: #ffffff;
    --page: #f2f2f2;
  }
  * { box-sizing: border-box; margin: 0; padding: 0; }
  html, body {
    width: 1043px;
    height: 1200px;
    overflow: hidden;
    background: var(--page);
    font-family: "Marcellus", Georgia, serif;
  }
  .backdrop {
    position: absolute;
    left: 21px;
    top: 200px;
    width: 1000px;
    height: 800px;
    background: var(--paper);
  }
  .repeat-grid {
    position: absolute;
    left: 43px;
    top: 4px;
    display: grid;
    grid-template-columns: repeat(10, 91.5px);
    grid-template-rows: repeat(8, 97px);
  }
  .tile {
    display: flex;
    align-items: center;
    justify-content: center;
  }
  .names {
    flex-direction: column;
    align-items: flex-start;
    color: var(--burgundy);
    font-size: 17px;
    line-height: 0.95;
    transform: rotate(-28deg);
  }
  .names .second { padding-left: 14px; }
  .names .amp {
    font-size: 8px;
    padding-left: 10px;
    line-height: 0.6;
  }
  .monogram {
    color: var(--gold);
    font-size: 24px;
    letter-spacing: 0.5px;
  }
  .names-feature {
    grid-column: 1 / 3;
    grid-row: 1 / 3;
    font-size: 44px;
  }
  .names-feature .second { padding-left: 34px; }
  .names-feature .amp { font-size: 16px; padding-left: 26px; }
  .monogram-feature {
    grid-column: 9 / 11;
    grid-row: 7 / 9;
    font-size: 62px;
  }
</style>
</head>
<body>
<main class="backdrop">
  <div class="repeat-grid">
    <div class="tile names names-feature"><span>Elena</span><span class="amp">&amp;</span><span class="second">Gavin</span></div>
    <div class="tile monogram monogram-feature">E&amp;G</div>

    <!-- row 1 -->
    <div class="tile names"><span>Elena</span><span class="amp">&amp;</span><span class="second">Gavin</span></div>
    <div class="tile monogram">E&amp;G</div>
    <div class="tile names"><span>Elena</span><span class="amp">&amp;</span><span class="second">Gavin</span></div>
    <div class="tile monogram">E&amp;G</div>
    <div class="tile names"><span>Elena</span><span class="amp">&amp;</span><span class="second">Gavin</span></div>
    <div class="tile monogram">E&amp;G</div>
    <div class="tile names"><span>Elena</span><span class="amp">&amp;</span><span class="second">Gavin</span></div>
    <div class="tile monogram">E&amp;G</div>
    <!-- row 2 -->
    <div class="tile monogram">E&amp;G</div>
    <div class="tile names"><span>Elena</span><span class="amp">&amp;</span><span class="second">Gavin</span></div>
    <div class="tile monogram">E&amp;G</div>
    <div class="tile names"><span>Elena</span><span class="amp">&amp;</span><span class="second">Gavin</span></div>
    <div class="tile monogram">E&amp;G</div>
    <div class="tile names"><span>Elena</span><span class="amp">&amp;</span><span class="second">Gavin</span></div>
    <div class="tile monogram">E&amp;G</div>
    <div class="tile names"><span>Elena</span><span class="amp">&amp;</span><span class="second">Gavin</span></div>
    <!-- row 3 -->
    <div class="tile names"><span>Elena</span><span class="amp">&amp;</span><span class="second">Gavin</span></div>
    <div class="tile monogram">E&amp;G</div>
    <div class="tile names"><span>Elena</span><span class="amp">&amp;</span><span class="second">Gavin</span></div>
    <div class="tile monogram">E&amp;G</div>
    <div class="tile names"><span>Elena</span><span class="amp">&amp;</span><span class="second">Gavin</span></div>
    <div class="tile monogram">E&amp;G</div>
    <div class="tile names"><span>Elena</span><span class="amp">&amp;</span><span class="second">Gavin</span></div>
    <div class="tile monogram">E&amp;G</div>
    <div class="tile names"><span>Elena</span><span class="amp">&amp;</span><span class="second">Gavin</span></div>
    <div class="tile monogram">E&amp;G</div>
    <!-- row 4 -->
    <div class="tile monogram">E&amp;G</div>
    <div class="tile names"><span>Elena</span><span class="amp">&amp;</span><span class="second">Gavin</span></div>
    <div class="tile monogram">E&amp;G</div>
    <div class="tile names"><span>Elena</span><span class="amp">&amp;</span><span class="second">Gavin</span></div>
    <div class="tile monogram">E&amp;G</div>
    <div class="tile names"><span>Elena</span><span class="amp">&amp;</span><span class="second">Gavin</span></div>
    <div class="tile monogram">E&amp;G</div>
    <div class="tile names"><span>Elena</span><span class="amp">&amp;</span><span class="second">Gavin</span></div>
    <div class="tile monogram">E&amp;G</div>
    <div class="tile names"><span>Elena</span><span class="amp">&amp;</span><span class="second">Gavin</span></div>
    <!-- row 5 -->
    <div class="tile names"><span>Elena</span><span class="amp">&amp;</span><span class="second">Gavin</span></div>
    <div class="tile monogram">E&amp;G</div>
    <div class="tile names"><span>Elena</span><span class="amp">&amp;</span><span class="second">Gavin</span></div>
    <div class="tile monogram">E&amp;G</div>
    <div class="tile names"><span>Elena</span><span class="amp">&amp;</span><span class="second">Gavin</span></div>
    <div class="tile monogram">E&amp;G</div>
    <div class="tile names"><span>Elena</span><span class="amp">&amp;</span><span class="second">Gavin</span></div>
    <div class="tile monogram">E&amp;G</div>
    <div class="tile names"><span>Elena</span><span class="amp">&amp;</span><span class="second">Gavin</span></div>
    <div class="tile monogram">E&amp;G</div>
    <!-- row 6 -->
    <div class="tile monogram">E&amp;G</div>
    <div class="tile names"><span>Elena</span><span class="amp">&amp;</span><span class="second">Gavin</span></div>
    <div class="tile monogram">E&amp;G</div>
    <div class="tile names"><span>Elena</span><span class="amp">&amp;</span><span class="second">Gavin</span></div>
    <div class="tile monogram">E&amp;G</div>
    <div class="tile names"><span>Elena</span><span class="amp">&amp;</span><span class="second">Gavin</span></div>
    <div class="tile monogram">E&amp;G</div>
    <div class="tile names"><span>Elena</span><span class="amp">&amp;</span><span class="second">Gavin</span></div>
    <div class="tile monogram">E&amp;G</div>
    <div class="tile names"><span>Elena</span><span class="amp">&amp;</span><span class="second">Gavin</span></div>
    <!-- row 7 -->
    <div class="tile names"><span>Elena</span><span class="amp">&amp;</span><span class="second">Gavin</span></div>
    <div class="tile monogram">E&amp;G</div>
    <div class="tile names"><span>Elena</span><span class="amp">&amp;</span><span class="second">Gavin</span></div>
    <div class="tile monogram">E&amp;G</div>
    <div class="tile names"><span>Elena</span><span class="amp">&amp;</span><span class="second">Gavin</span></div>
    <div class="tile monogram">E&amp;G</div>
    <div class="tile names"><span>Elena</span><span class="amp">&amp;</span><span class="second">Gavin</span></div>
    <div class="tile monogram">E&amp;G</div>
    <!-- row 8 -->
    <div class="tile monogram">E&amp;G</div>
    <div class="tile names"><span>Elena</span><span class="amp">&amp;</span><span class="second">Gavin</span></div>
    <div class="tile monogram">E&amp;G</div>
    <div class="tile names"><span>Elena</span><span class="amp">&amp;</span><span class="second">Gavin</span></div>
    <div class="tile monogram">E&amp;G</div>
    <div class="tile names"><span>Elena</span><span class="amp">&amp;</span><span class="second">Gavin</span></div>
    <div class="tile monogram">E&amp;G</div>
    <div class="tile names"><span>Elena</span><span class="amp">&amp;</span><span class="second">Gavin</span></div>
  </div>
</main>
</body>
</html>
```